Flyer Design Project

I teach a spiritual dance class and I want to explain what it is and who it would benefit. I would love to have a sticker for where I am teaching it because that can change.

I want it to be a bit spiritual, very hip and cool, and transformational!!

Target Market(s)

Mostly women (or enlightened men)! all ages

Requirements
Must have
• Lumen Sway

We need to move. We need to breathe. We need to smile and giggle and laugh and cry and scream and make noise and dance. It's not about burning calories and it is not about reaching a goal. It's about feeling. It's about taking the time to nurture our souls. It's about finding joy and peace in our hectic lives. It's about healing.

Lumen Sway is a wildly fun, uplifting, emotionally cleansing, refreshing, restorative, heart-opening, transformational dance celebration that is sure to leave you relaxed and smiling. All ages, shapes and sizes are welcome with no experience necessary.
About Carla:

I was certified at Vestora in both “Open Heart Motion Flow” and “Tidal Steps” and am a
certified Group Exercise Instructor with the National Council for Active Movement Trainers (NCAM). I also have a black belt in Tae Kwon Do. As of 2013, I will be a certified holistic health and nutrition coach and am the creator of the popular Bright, Bold, and Breezy page on Friendspace.
For more info:
Carlabrennick@mailvista.net

Classes and workshops to energize your body, mind, and spirit.

```html
<!DOCTYPE html>
<html lang="en">
<head>
<meta charset="utf-8">
<title>Lumen Sway – Dance Classes Flyer</title>
<link rel="stylesheet" href="https://fonts.googleapis.com/css2?family=Arimo:wght@400;700&family=Righteous&display=swap">
<style>
  :root {
    --pink: #e81d9c;
    --pink-deep: #b3127a;
    --white: #ffffff;
    --navy: #0b0f2e;
    --purple: #8b2bd6;
    --violet: #5a1aa8;
    --lime: #b6f03a;
    --yellow: #e9f55a;
    --sky: #3aa9f0;
    --blue: #1d4fd8;
  }
  html, body {
    margin: 0;
    padding: 0;
    width: 848px;
    height: 1200px;
    overflow: hidden;
    background: #ffffff;
  }
  .flyer {
    position: relative;
    width: 848px;
    height: 1200px;
    overflow: hidden;
    font-family: "Arimo", Arial, sans-serif;
    color: var(--white);
  }
  .backdrop {
    position: absolute;
    inset: 0;
    width: 848px;
    height: 1200px;
  }
  .title-banner {
    position: absolute;
    left: 118px;
    top: 150px;
    width: 672px;
    height: 108px;
    background: var(--pink);
    transform: rotate(-8deg);
    transform-origin: left bottom;
    box-shadow: 0 0 0 4px rgba(255,255,255,0.15);
  }
  .title {
    position: absolute;
    left: 120px;
    top: 128px;
    width: 672px;
    margin: 0;
    font-family: "Righteous", "Arial Black", sans-serif;
    font-size: 84px;
    font-weight: 400;
    line-height: 1;
    letter-spacing: 1px;
    text-align: center;
    color: var(--white);
    transform: rotate(-8deg);
    transform-origin: left bottom;
    -webkit-text-stroke: 2px var(--pink-deep);
  }
  .side-title {
    position: absolute;
    left: 22px;
    top: 1180px;
    margin: 0;
    font-family: "Righteous", "Arial Black", sans-serif;
    font-size: 84px;
    font-weight: 400;
    line-height: 1;
    white-space: nowrap;
    color: var(--white);
    transform: rotate(-90deg);
    transform-origin: left top;
    letter-spacing: 1px;
  }
  .copy {
    position: absolute;
    left: 112px;
    width: 724px;
    margin: 0;
    text-align: center;
    font-size: 20.5px;
    line-height: 26.5px;
  }
  .copy-intro { top: 244px; }
  .copy-intro .lead { display: block; padding-left: 140px; }
  .copy-pitch { top: 438px; color: var(--pink); }
  .copy-pitch strong { font-weight: 700; }
  .about { top: 590px; }
  .about-heading {
    display: block;
    color: var(--pink);
    font-weight: 400;
  }
  .contact {
    position: absolute;
    right: 24px;
    top: 990px;
    text-align: right;
    font-family: "Righteous", "Arial Black", sans-serif;
    font-size: 27px;
    line-height: 36px;
    color: var(--white);
    -webkit-text-stroke: 1px var(--pink);
    text-shadow: 0 0 6px var(--pink), 0 0 2px var(--pink);
  }
  .contact-label { display: block; }
  .contact-email { display: block; font-size: 25px; }
  .tagline {
    position: absolute;
    right: 24px;
    top: 1104px;
    margin: 0;
    text-align: right;
    font-family: "Righteous", "Arial Black", sans-serif;
    font-size: 29px;
    line-height: 35px;
    color: var(--white);
    -webkit-text-stroke: 1px var(--pink);
    text-shadow: 0 0 7px var(--pink), 0 0 3px var(--pink);
  }
</style>
</head>
<body>
<main class="flyer">
  <svg class="backdrop" viewBox="0 0 848 1200" xmlns="http://www.w3.org/2000/svg">
    <defs>
      <linearGradient id="base-wash" x1="0" y1="0" x2="1" y2="1">
        <stop offset="0" stop-color="#7be03a"/>
        <stop offset="0.35" stop-color="#2ab3e6"/>
        <stop offset="0.7" stop-color="#6d2bd0"/>
        <stop offset="1" stop-color="#3a0f7a"/>
      </linearGradient>
      <radialGradient id="orb" cx="0.5" cy="0.5" r="0.5">
        <stop offset="0" stop-color="#0b0f2e" stop-opacity="0.96"/>
        <stop offset="0.85" stop-color="#121848" stop-opacity="0.9"/>
        <stop offset="1" stop-color="#1b2a6e" stop-opacity="0.85"/>
      </radialGradient>
      <linearGradient id="floor" x1="0" y1="0" x2="0" y2="1">
        <stop offset="0" stop-color="#7a2ad0" stop-opacity="0"/>
        <stop offset="0.35" stop-color="#8b2bd6" stop-opacity="0.75"/>
        <stop offset="1" stop-color="#b04ae6"/>
      </linearGradient>
      <radialGradient id="dancer-glow" cx="0.5" cy="0.6" r="0.6">
        <stop offset="0" stop-color="#2a0c4e" stop-opacity="0.85"/>
        <stop offset="1" stop-color="#2a0c4e" stop-opacity="0"/>
      </radialGradient>
      <radialGradient id="flourish" cx="0.5" cy="0.5" r="0.5">
        <stop offset="0" stop-color="#ffffff" stop-opacity="0.35"/>
        <stop offset="1" stop-color="#ffffff" stop-opacity="0"/>
      </radialGradient>
    </defs>

    <rect class="wash" width="848" height="1200" fill="url(#base-wash)"/>

    <g class="light-rays">
      <polygon points="0,0 150,0 0,330" fill="#8ef03c"/>
      <polygon points="150,0 300,0 0,420 0,330" fill="#d8f544"/>
      <polygon points="300,0 420,0 0,560 0,420" fill="#e9f55a" opacity="0.85"/>
      <polygon points="520,0 700,0 520,360" fill="#4fd0c8" opacity="0.7"/>
      <polygon points="700,0 848,0 848,120 640,420" fill="#3aa9f0"/>
      <polygon points="848,120 848,360 700,520" fill="#9ee0ff" opacity="0.8"/>
      <polygon points="848,360 848,640 640,560" fill="#2d6ee6"/>
      <polygon points="848,640 848,860 560,620" fill="#7b3ae0"/>
      <polygon points="0,560 0,760 260,520" fill="#1d4fd8"/>
      <polygon points="0,760 0,980 240,640" fill="#4a2bd0"/>
      <polygon points="0,980 0,1200 220,760" fill="#6d1fc0"/>
    </g>

    <rect class="side-band" x="0" y="380" width="108" height="820" fill="#1d3ad8" opacity="0.55"/>

    <circle class="orb" cx="479" cy="436" r="404" fill="url(#orb)"/>
    <circle class="orb-ring" cx="479" cy="436" r="404" fill="none" stroke="#3a6ee8" stroke-opacity="0.5" stroke-width="3"/>

    <rect class="dance-floor" x="0" y="760" width="848" height="440" fill="url(#floor)"/>
    <g class="floor-streaks" stroke="#e4a6ff" stroke-opacity="0.45" stroke-width="6">
      <line x1="130" y1="1150" x2="848" y2="1090"/>
      <line x1="130" y1="1180" x2="848" y2="1130"/>
      <line x1="360" y1="1040" x2="848" y2="1000"/>
    </g>

    <rect class="dancers" role="img" aria-label="Silhouettes of two women dancing freely on a glowing purple floor"
          x="150" y="800" width="520" height="400" fill="url(#dancer-glow)"/>

    <ellipse class="script-flourish" role="img" aria-label="Faint decorative script initial behind the title"
             cx="120" cy="210" rx="95" ry="130" fill="url(#flourish)"/>
  </svg>

  <div class="title-banner" aria-hidden="true"></div>
  <h1 class="title">LUMEN SWAY</h1>

  <p class="side-title" aria-hidden="true">LUMEN SWAY</p>

  <p class="copy copy-intro">
    <span class="lead">We need to move.</span>
    We need to breathe. We need to smile and giggle and laugh and cry and scream and make noise and dance. It's not about burning calories and it is not about reaching a goal. It's about feeling. It's about taking the time to nurture our souls. It's about finding joy and peace in our hectic lives. It's about healing.
  </p>

  <p class="copy copy-pitch">
    <strong>Lumen Sway</strong> is a wildly fun, uplifting, emotionally cleansing, refreshing, restorative, heart-opening, transformational dance celebration that is sure to leave you relaxed and smiling. All ages, shapes and sizes are welcome with no experience necessary.
  </p>

  <p class="copy about">
    <span class="about-heading">ABOUT CARLA:</span>
    I was certified at Vestora in both “Open Heart Motion Flow” and “Tidal Steps” and am a certified Group Exercise Instructor with the National Council for Active Movement Trainers (NCAM). I also have a black belt in Tae Kwon Do. As of 2013, I will be a certified holistic health and nutrition coach and am the creator of the popular Bright, Bold, and Breezy page on Friendspace.
  </p>

  <p class="contact">
    <span class="contact-label">FOR MORE INFO:</span>
    <span class="contact-email">Carlabrennick@mailvista.net</span>
  </p>

  <p class="tagline">Classes and workshops to energize<br>your body, mind, and spirit.</p>
</main>
</body>
</html>
```